Harborline Wonder Evenings - A magic website for a monthly modern magic show

Looking to build a website to promote my new monthly magic show

Sites like this. https://loftwanderer-example.com/ https://sevenunlikelywondersrevue-example.com/

Target Market(s)

18-65 year old men and women who enjoy live entertainment especially magic

Industry/Entity Type

Entertainment

Coding

Coded - Design and coding required

Number of Pages Required

3 page

Colors

Designer to choose colors to be used in the design.

Requirements
Must have
• Wanting a wordpress site.
• Contact form, media section for photos and videos to be posted.
• A “reviews/testimonials” section.

```html
<!DOCTYPE html>
<html lang="en">
<head>
<meta charset="utf-8">
<title>Harborline Wonder Evenings – Website Design</title>
<link href="https://fonts.googleapis.com/css2?family=Lato:wght@400;700;900&family=Montserrat:wght@400;500&display=swap" rel="stylesheet">
<style>
:root{
  --gold:#c39150;
  --gold-light:#d6a762;
  --ink:#0b0a0c;
  --navy:#16233f;
  --navy-deep:#0a1020;
  --brown:#4a3422;
  --brown-deep:#1b130d;
  --white:#ffffff;
  --muted:#d9d9d9;
  --star:#f2a516;
}
*{box-sizing:border-box;margin:0;padding:0}
html,body{width:977px;height:1200px;overflow:hidden;background:var(--white)}
body{position:relative;font-family:"Lato",sans-serif}

.brand-mark{position:absolute;left:380px;top:56px;width:220px;display:flex;align-items:center;gap:10px;justify-content:center}
.brand-mark__dot{width:38px;height:38px;border:3px solid var(--gold);border-radius:50%;flex:none}
.brand-mark__name{font-family:"Montserrat",sans-serif;font-weight:500;font-size:17px;color:var(--gold);white-space:nowrap}

.site{position:absolute;width:715px;transform:scale(.5625);transform-origin:top left;background:var(--ink);color:var(--white);overflow:hidden}
.site--long{left:63px;top:164px;height:1806px}
.site--short{left:531px;top:163px;height:1630px}

.section{position:relative;width:715px}
.photo{position:absolute;inset:0}

/* Hero */
.hero .photo{background:radial-gradient(ellipse at 70% 40%,#2a3d66 0%,var(--navy) 35%,var(--navy-deep) 80%)}
.site--long .hero{height:360px}
.site--short .hero{height:320px}
.nav{position:absolute;left:0;top:0;width:715px;height:80px}
.nav__logo{position:absolute;left:66px;top:22px;display:flex;align-items:center;gap:6px}
.nav__logo-dot{width:34px;height:34px;border:2px solid var(--gold);border-radius:50%}
.nav__logo-name{font-family:"Montserrat",sans-serif;font-size:10px;color:var(--gold);font-weight:500}
.nav__menu{position:absolute;left:234px;top:33px;display:flex;gap:20px;font-family:"Montserrat",sans-serif;font-size:11px;letter-spacing:.2px;list-style:none}
.nav__menu .is-active{color:var(--gold)}
.hero__title{position:absolute;left:76px;font-family:"Lato",sans-serif;font-weight:900;font-size:31px;color:var(--gold)}
.hero__text{position:absolute;left:76px;width:230px;font-size:12px;line-height:20.5px}
.btn{position:absolute;background:var(--gold);color:var(--white);display:flex;align-items:center;justify-content:center;font-size:13px}
.hero__btn{left:76px;width:109px;height:35px;font-size:14px}
.site--long .hero__title{top:121px}.site--long .hero__text{top:170px}.site--long .hero__btn{top:249px}
.site--short .hero__title{top:109px}.site--short .hero__text{top:158px}.site--short .hero__btn{top:240px}
.slider-dots{position:absolute;left:656px;top:148px;display:flex;flex-direction:column;gap:7px}
.slider-dots span{width:7px;height:7px;border-radius:50%;background:var(--white)}
.slider-dots span:first-child{background:var(--gold)}

/* About */
.about .photo{background:linear-gradient(100deg,#5b4230 0%,var(--brown) 30%,#2b1e15 65%,var(--brown-deep) 100%)}
.site--long .about{height:385px}
.site--short .about{height:322px}
.section-title{font-family:"Montserrat",sans-serif;font-weight:400;font-size:24px}
.about__title{position:absolute;left:66px}
.about__text{position:absolute;left:66px;width:340px;font-family:"Montserrat",sans-serif;font-size:9.6px;line-height:20.5px;text-align:justify;color:var(--muted)}
.about__btn{left:66px;width:100px;height:35px;font-family:"Montserrat",sans-serif;font-size:12px}
.site--long .about__title{top:103px}.site--long .about__text{top:140px}.site--long .about__btn{top:304px}
.site--short .about__title{top:60px;left:80px}.site--short .about__text{top:97px;left:80px}.site--short .about__btn{top:261px;left:80px}

.curve{position:absolute;left:0;width:715px;height:60px;z-index:2}

/* Media */
.media .photo{background:radial-gradient(ellipse at 50% 70%,#2d2f36 0%,#141417 55%,var(--ink) 100%)}
.site--long .media{height:355px}
.site--short .media{height:321px}
.media__title{position:absolute;left:0;width:715px;text-align:center}
.site--long .media__title{top:76px}
.site--short .media__title{top:40px}
.media__stage{position:absolute;left:0;width:715px;height:165px}
.site--long .media__stage{top:135px}
.site--short .media__stage{top:100px}
.media__item{position:absolute;border:2px solid var(--white)}
.media__item--left{left:68px;top:10px;width:155px;height:143px;background:linear-gradient(135deg,#e8d8c8,#c98f6e 55%,#3d2a22)}
.media__item--center{left:223px;top:0;width:269px;height:160px;background:linear-gradient(120deg,#6d4a35,#3a2a26 45%,#1f1a1a)}
.media__item--right{left:492px;top:10px;width:157px;height:143px;background:linear-gradient(120deg,#7a4638,#3c2c2a 50%,#18161a)}
.media__arrow{position:absolute;top:68px;width:36px;height:32px;background:var(--white);display:flex;align-items:center;justify-content:center}
.media__arrow--prev{left:207px}.media__arrow--next{left:474px}
.media__play{position:absolute;left:343px;top:73px;width:30px;height:30px;border-radius:50%;background:var(--gold);display:flex;align-items:center;justify-content:center}

/* Testimonials */
.testimonials .photo{background:radial-gradient(ellipse at 20% 60%,#2a2216 0%,#0d0b09 45%,var(--ink) 100%)}
.site--long .testimonials{height:380px}
.site--short .testimonials{height:367px}
.testimonials__title{position:absolute;left:0;width:715px;text-align:center}
.site--long .testimonials__title{top:46px}
.site--short .testimonials__title{top:36px}
.review{position:absolute;width:210px;height:200px;background:var(--white)}
.site--long .review{top:118px}
.site--short .review{top:103px}
.review--one{left:135px}.review--two{left:380px}
.site--short .review--one{left:128px}.site--short .review--two{left:373px}
.review__quote{height:102px;background:var(--gold);position:relative;padding:12px 12px 0;font-family:"Montserrat",sans-serif;font-size:10px;line-height:21px;text-align:center}
.review__mark{position:absolute;font-family:"Montserrat",sans-serif;font-size:18px;line-height:1;color:#f1dfc4}
.review__mark--open{left:6px;top:4px}.review__mark--close{right:12px;bottom:10px}
.review__avatar{position:absolute;left:76px;top:78px;width:58px;height:58px;border-radius:50%;border:2px solid var(--white);background:linear-gradient(160deg,#b9a08c,#5d4a40)}
.review__name{position:absolute;top:143px;width:210px;text-align:center;font-family:"Montserrat",sans-serif;font-size:15.5px;color:#333}
.review__stars{position:absolute;top:168px;width:210px;text-align:center;font-size:9px;letter-spacing:1px;color:var(--star)}
.pager{position:absolute;left:333px;display:flex;gap:9px}
.site--long .pager{top:353px}
.site--short .pager{top:337px}
.pager span{width:9px;height:9px;border-radius:50%;background:var(--white)}

/* Contact */
.contact .photo{background:linear-gradient(180deg,#0c0b0b,#14110f 60%,#0a0909)}
.site--long .contact{height:326px}
.site--short .contact{height:300px}
.contact__inner{position:absolute;left:0;width:715px;height:260px}
.site--long .contact__inner{top:61px}
.site--short .contact__inner{top:28px}
.contact__title{position:absolute;left:66px;top:0}
.form__title{position:absolute;left:418px;top:0}
.site--short .contact__title{left:65px}
.info{position:absolute;left:70px;display:flex;align-items:center;gap:16px;font-family:"Montserrat",sans-serif;font-size:13px;line-height:15px}
.info__icon{width:32px;height:32px;border-radius:50%;background:var(--gold);display:flex;align-items:center;justify-content:center;flex:none}
.info--address{top:54px}.info--phone{top:110px}.info--email{top:163px}
.field{position:absolute;border:1px solid #8a6a40;height:27px;padding:6px 18px;font-family:"Montserrat",sans-serif;font-size:10.5px;color:var(--gold)}
.field--first{left:344px;top:51px;width:146px}
.field--last{left:497px;top:51px;width:146px}
.field--phone{left:344px;top:93px;width:146px}
.field--email{left:497px;top:93px;width:146px}
.field--message{left:344px;top:133px;width:299px;height:40px}
.form__submit{left:455px;top:193px;width:81px;height:24px}
.footer__copy{position:absolute;left:68px;top:243px;font-size:7.5px;color:var(--white)}
.footer__code{position:absolute;left:650px;top:243px;font-size:6.5px;color:#bbb}
</style>
</head>
<body>

<div class="brand-mark">
  <span class="brand-mark__dot"></span>
  <span class="brand-mark__name">Harborline Wonder</span>
</div>

<!-- Desktop layout with curved dividers -->
<div class="site site--long">
  <section class="section hero">
    <div class="photo" role="img" aria-label="Magician in white gloves lifting a wand above a top hat against a starry blue backdrop"></div>
    <header class="nav">
      <div class="nav__logo"><span class="nav__logo-dot"></span><span class="nav__logo-name">Harborline Wonder</span></div>
      <ul class="nav__menu">
        <li class="is-active">HOME</li><li>EVENTS</li><li>PRIVATE EVENTS</li><li>ABOUT</li><li>REVIEWS</li><li>CONTACT</li>
      </ul>
    </header>
    <h1 class="hero__title">Harborline Wonder</h1>
    <p class="hero__text">Lorem ipsum dolor sit amet, consectetur adipiscing elit, sed do eiusmod tempor incididunt ut labore et dolore .</p>
    <a class="btn hero__btn">Book Now</a>
    <div class="slider-dots"><span></span><span></span><span></span></div>
  </section>

  <section class="section about">
    <div class="photo" role="img" aria-label="Smiling magician in a dark suit fanning playing cards beside a glowing crystal ball"></div>
    <svg class="curve" style="top:-14px" viewBox="0 0 715 60" preserveAspectRatio="none" aria-hidden="true">
      <path d="M0 40 Q357 -12 715 40 L715 60 L0 60 Z" fill="#4a3422"/>
      <path d="M0 40 Q357 -12 715 40 L715 37 Q357 -2 0 26 Z" fill="#c39150"/>
      <path d="M0 42 Q357 -6 715 42" stroke="#fff" stroke-width="1" fill="none"/>
    </svg>
    <h2 class="section-title about__title">About Harborline Wonder</h2>
    <p class="about__text">Lorem ipsum dolor sit amet, consectetur adipiscing elit, sed do eiusmod tempor incididunt ut labore et dolore magna aliqua. Quis ipsum suspendisse ultrices gravida. Risus commodo viverra maecenas accumsan lacus vel facilisis. Lorem ipsum dolor sit amet, consectetur adipiscing elit, sed do eiusmod tempor incididunt ut labore et dolore magna aliqua. Quis ipsum suspendisse ultrices gravida. Risus commodo viverra maecenas accumsan lacus vel facilisis.</p>
    <a class="btn about__btn">Read More</a>
    <svg class="curve" style="bottom:-22px" viewBox="0 0 715 60" preserveAspectRatio="none" aria-hidden="true">
      <path d="M0 0 L715 0 L715 8 Q357 58 0 10 Z" fill="#2a1e15"/>
      <path d="M0 10 Q357 58 715 8 L715 24 Q357 66 0 18 Z" fill="#c39150"/>
    </svg>
  </section>

  <section class="section media">
    <div class="photo" role="img" aria-label="Dark stage backdrop with a performer in a suit and soft smoke"></div>
    <h2 class="section-title media__title">Media</h2>
    <div class="media__stage">
      <div class="media__item media__item--left" role="img" aria-label="Hand holding a solved colour cube"></div>
      <div class="media__item media__item--center" role="img" aria-label="Video still of the magician performing close-up for guests"></div>
      <div class="media__item media__item--right" role="img" aria-label="Magician holding a banknote and a pocket watch"></div>
      <div class="media__arrow media__arrow--prev"><svg width="16" height="12" viewBox="0 0 16 12"><path d="M15 6H2M6 1L1 6l5 5" stroke="#c39150" stroke-width="1.5" fill="none"/></svg></div>
      <div class="media__arrow media__arrow--next"><svg width="16" height="12" viewBox="0 0 16 12"><path d="M1 6h13M10 1l5 5-5 5" stroke="#c39150" stroke-width="1.5" fill="none"/></svg></div>
      <div class="media__play"><svg width="10" height="12" viewBox="0 0 10 12"><path d="M1 0l9 6-9 6z" fill="#fff"/></svg></div>
    </div>
  </section>

  <section class="section testimonials">
    <div class="photo" role="img" aria-label="Black background with scattered golden bokeh sparkles"></div>
    <svg class="curve" style="top:-28px" viewBox="0 0 715 60" preserveAspectRatio="none" aria-hidden="true">
      <path d="M0 40 Q357 -12 715 40 L715 60 L0 60 Z" fill="#0d0b09"/>
      <path d="M0 40 Q357 -12 715 40 L715 37 Q357 -2 0 26 Z" fill="#c39150"/>
      <path d="M0 42 Q357 -6 715 42" stroke="#fff" stroke-width="1" fill="none"/>
    </svg>
    <h2 class="section-title testimonials__title">Testimonials</h2>
    <article class="review review--one">
      <div class="review__quote"><span class="review__mark review__mark--open">&ldquo;</span>Lorem ipsum dolor sit amet, consectetur adipiscing elit, sed do eiusmod tempor incididunt ut labore<span class="review__mark review__mark--close">&rdquo;</span></div>
      <div class="review__avatar" role="img" aria-label="Portrait of William"></div>
      <p class="review__name">William</p>
      <p class="review__stars">★★★★★</p>
    </article>
    <article class="review review--two">
      <div class="review__quote"><span class="review__mark review__mark--open">&ldquo;</span>Lorem ipsum dolor sit amet, consectetur adipiscing elit, sed do eiusmod tempor incididunt ut labore<span class="review__mark review__mark--close">&rdquo;</span></div>
      <div class="review__avatar" role="img" aria-label="Portrait of Charlotte"></div>
      <p class="review__name">Charlotte</p>
      <p class="review__stars">★★★★★</p>
    </article>
    <div class="pager"><span></span><span></span><span></span></div>
  </section>

  <section class="section contact">
    <div class="photo" role="img" aria-label="Dim dark background of a stage table"></div>
    <svg class="curve" style="top:-30px" viewBox="0 0 715 60" preserveAspectRatio="none" aria-hidden="true">
      <path d="M0 0 L715 0 L715 8 Q357 58 0 10 Z" fill="#0b0a0c"/>
      <path d="M0 10 Q357 58 715 8 L715 24 Q357 66 0 18 Z" fill="#c39150"/>
    </svg>
    <div class="contact__inner">
      <h2 class="section-title contact__title">Contact Us</h2>
      <h2 class="section-title form__title">Get in Touch</h2>
      <div class="info info--address"><span class="info__icon"><svg width="12" height="16" viewBox="0 0 12 16"><path d="M6 0a6 6 0 0 0-6 6c0 4.5 6 10 6 10s6-5.5 6-10a6 6 0 0 0-6-6zm0 8.5A2.5 2.5 0 1 1 6 3.5a2.5 2.5 0 0 1 0 5z" fill="#fff"/></svg></span><span>2310 Lantern Row<br>Ave,</span></div>
      <div class="info info--phone"><span class="info__icon"><svg width="14" height="14" viewBox="0 0 14 14"><path d="M3 0l2.5 3.2-1.6 2.1a8 8 0 0 0 4.8 4.8l2.1-1.6L14 11l-1.5 2.5C6 14 0 8 .5 1.5z" fill="#fff"/></svg></span><span>Tel:&nbsp; (555) 010-2244</span></div>
      <div class="info info--email"><span class="info__icon"><svg width="14" height="10" viewBox="0 0 14 10"><rect width="14" height="10" fill="#fff"/><path d="M0 0l7 6 7-6" stroke="#c39150" fill="none"/></svg></span><span>Email:info@harborlinewonder.com</span></div>
      <div class="field field--first">Fast Name</div>
      <div class="field field--last">Last Name</div>
      <div class="field field--phone">Phone</div>
      <div class="field field--email">Email</div>
      <div class="field field--message">Message</div>
      <a class="btn form__submit">Submit</a>
      <p class="footer__copy">Copyrights © 2019 Copyrights Company Name | All Rights Reserved</p>
      <p class="footer__code">c36</p>
    </div>
  </section>
</div>

<!-- Compact layout with straight section edges -->
<div class="site site--short">
  <section class="section hero">
    <div class="photo" role="img" aria-label="Magician in white gloves lifting a wand above a top hat against a starry blue backdrop"></div>
    <header class="nav">
      <div class="nav__logo"><span class="nav__logo-dot"></span><span class="nav__logo-name">Harborline Wonder</span></div>
      <ul class="nav__menu">
        <li class="is-active">HOME</li><li>EVENTS</li><li>PRIVATE EVENTS</li><li>ABOUT</li><li>REVIEWS</li><li>CONTACT</li>
      </ul>
    </header>
    <h1 class="hero__title">Harborline Wonder</h1>
    <p class="hero__text">Lorem ipsum dolor sit amet, consectetur adipiscing elit, sed do eiusmod tempor incididunt ut labore et dolore .</p>
    <a class="btn hero__btn">Book Now</a>
    <div class="slider-dots"><span></span><span></span><span></span></div>
  </section>

  <section class="section about">
    <div class="photo" role="img" aria-label="Smiling magician in a dark suit fanning playing cards beside a glowing crystal ball"></div>
    <h2 class="section-title about__title">About Harborline Wonder</h2>
    <p class="about__text">Lorem ipsum dolor sit amet, consectetur adipiscing elit, sed do eiusmod tempor incididunt ut labore et dolore magna aliqua. Quis ipsum suspendisse ultrices gravida. Risus commodo viverra maecenas accumsan lacus vel facilisis. Lorem ipsum dolor sit amet, consectetur adipiscing elit, sed do eiusmod tempor incididunt ut labore et dolore magna aliqua. Quis ipsum suspendisse ultrices gravida. Risus commodo viverra maecenas accumsan lacus vel facilisis.</p>
    <a class="btn about__btn">Read More</a>
  </section>

  <section class="section media">
    <div class="photo" role="img" aria-label="Dark stage backdrop with a performer in a suit and soft smoke"></div>
    <h2 class="section-title media__title">Media</h2>
    <div class="media__stage">
      <div class="media__item media__item--left" role="img" aria-label="Hand holding a solved colour cube"></div>
      <div class="media__item media__item--center" role="img" aria-label="Video still of the magician performing close-up for guests"></div>
      <div class="media__item media__item--right" role="img" aria-label="Magician holding a banknote and a pocket watch"></div>
      <div class="media__arrow media__arrow--prev"><svg width="16" height="12" viewBox="0 0 16 12"><path d="M15 6H2M6 1L1 6l5 5" stroke="#c39150" stroke-width="1.5" fill="none"/></svg></div>
      <div class="media__arrow media__arrow--next"><svg width="16" height="12" viewBox="0 0 16 12"><path d="M1 6h13M10 1l5 5-5 5" stroke="#c39150" stroke-width="1.5" fill="none"/></svg></div>
      <div class="media__play"><svg width="10" height="12" viewBox="0 0 10 12"><path d="M1 0l9 6-9 6z" fill="#fff"/></svg></div>
    </div>
  </section>

  <section class="section testimonials">
    <div class="photo" role="img" aria-label="Black background with scattered golden bokeh sparkles"></div>
    <h2 class="section-title testimonials__title">Testimonials</h2>
    <article class="review review--one">
      <div class="review__quote"><span class="review__mark review__mark--open">&ldquo;</span>Lorem ipsum dolor sit amet, consectetur adipiscing elit, sed do eiusmod tempor incididunt ut labore<span class="review__mark review__mark--close">&rdquo;</span></div>
      <div class="review__avatar" role="img" aria-label="Portrait of William"></div>
      <p class="review__name">William</p>
      <p class="review__stars">★★★★★</p>
    </article>
    <article class="review review--two">
      <div class="review__quote"><span class="review__mark review__mark--open">&ldquo;</span>Lorem ipsum dolor sit amet, consectetur adipiscing elit, sed do eiusmod tempor incididunt ut labore<span class="review__mark review__mark--close">&rdquo;</span></div>
      <div class="review__avatar" role="img" aria-label="Portrait of Charlotte"></div>
      <p class="review__name">Charlotte</p>
      <p class="review__stars">★★★★★</p>
    </article>
    <div class="pager"><span></span><span></span><span></span></div>
  </section>

  <section class="section contact">
    <div class="photo" role="img" aria-label="Dim dark background of a stage table"></div>
    <div class="contact__inner">
      <h2 class="section-title contact__title">Contact Us</h2>
      <h2 class="section-title form__title">Get in Touch</h2>
      <div class="info info--address"><span class="info__icon"><svg width="12" height="16" viewBox="0 0 12 16"><path d="M6 0a6 6 0 0 0-6 6c0 4.5 6 10 6 10s6-5.5 6-10a6 6 0 0 0-6-6zm0 8.5A2.5 2.5 0 1 1 6 3.5a2.5 2.5 0 0 1 0 5z" fill="#fff"/></svg></span><span>2310 Lantern Row<br>Ave,</span></div>
      <div class="info info--phone"><span class="info__icon"><svg width="14" height="14" viewBox="0 0 14 14"><path d="M3 0l2.5 3.2-1.6 2.1a8 8 0 0 0 4.8 4.8l2.1-1.6L14 11l-1.5 2.5C6 14 0 8 .5 1.5z" fill="#fff"/></svg></span><span>Tel:&nbsp; (555) 010-2244</span></div>
      <div class="info info--email"><span class="info__icon"><svg width="14" height="10" viewBox="0 0 14 10"><rect width="14" height="10" fill="#fff"/><path d="M0 0l7 6 7-6" stroke="#c39150" fill="none"/></svg></span><span>Email:info@harborlinewonder.com</span></div>
      <div class="field field--first">Fast Name</div>
      <div class="field field--last">Last Name</div>
      <div class="field field--phone">Phone</div>
      <div class="field field--email">Email</div>
      <div class="field field--message">Message</div>
      <a class="btn form__submit">Submit</a>
      <p class="footer__copy">Copyrights © 2019 Copyrights Company Name | All Rights Reserved</p>
      <p class="footer__code">c36</p>
    </div>
  </section>
</div>

</body>
</html>
```